I need a new business card design for my pharmacy.

I need a business card design. I will include my logo.
The card needs to be readable. I prefer to have my logo on one side along with my website, the other side includes the other information. Please use combination of black, neon green, white, and silver. This needs to catch the eye but yet be clearly visible and legible. Thanks

Industry/Entity Type

Pharmacy

Contact Information for Business Card

It needs to have the following information listed:
Vel's Apothecary Owner/Pharm D.
7143 North Birch Lane
Sioux Falls, SD 57362
Phone 605-318-6027
Fax 605-318-6025
email: vel@velsapothecary.example
www.velsapothecary.example
Store hours Monday-Friday 8 am- 7 pm
Saturday 8 am- 12 pm
Sunday Closed
Please utilize the colors black, white, and neon green, maybe silver.

Requirements
Must have
• It needs to be easily readable!
Nice to have
• It should catch the eye.
Should not have
• Do not use any other colors except listed: black, neon green, white, & silver.

```html
<!DOCTYPE html>
<html lang="en">
<head>
<meta charset="utf-8">
<title>Vel's Apothecary – Business Card</title>
<link rel="stylesheet" href="https://fonts.googleapis.com/css2?family=Questrial&family=Open+Sans:wght@600&display=swap">
<style>
  :root {
    --neon: #16e60f;
    --neon-light: #2cf020;
    --silver: #e6e6e6;
    --silver-dark: #cfcfcf;
    --ink: #1c1c1c;
    --ink-soft: #333333;
    --white: #ffffff;
    --mark-grey: #8c8c8c;
    --page: #ffffff;
  }
  * { box-sizing: border-box; margin: 0; padding: 0; }
  html, body {
    width: 1200px; height: 1000px; overflow: hidden;
    background: var(--page);
  }
  .card {
    position: absolute; left: 10px; top: 137px;
    width: 1178px; height: 723px;
    box-shadow: 0 2px 8px rgba(0,0,0,0.45);
    font-family: "Questrial", sans-serif;
    overflow: hidden;
  }
  .band { position: absolute; left: 0; width: 100%; }
  .band--top { top: 0; height: 168px; background: radial-gradient(ellipse at 50% 40%, var(--neon-light), var(--neon)); }
  .band--middle { top: 168px; height: 327px; background: linear-gradient(180deg, #efefef, var(--silver) 60%, #dedede); }
  .band--bottom { top: 495px; height: 228px; background: radial-gradient(ellipse at 40% 50%, var(--neon-light), var(--neon)); }
  .stripes {
    position: absolute; right: 0; width: 348px;
    background: repeating-linear-gradient(180deg, rgba(230,230,230,0.85) 0 4px, transparent 4px 9px);
  }
  .stripes--top { top: 0; height: 168px; }
  .stripes--middle { top: 168px; height: 327px; opacity: 0.35; }
  .stripes--bottom { top: 495px; height: 228px; }

  .title {
    position: absolute; left: 100px; top: 48px;
    font-size: 53px; color: var(--ink); font-weight: 400; letter-spacing: -0.5px;
  }
  .contact { position: absolute; display: flex; align-items: flex-start; gap: 16px; color: var(--ink-soft); font-size: 31px; line-height: 38px; }
  .contact svg { flex: none; fill: var(--ink-soft); }
  .contact--address { left: 100px; top: 196px; }
  .contact--address svg { margin-top: 16px; }
  .contact--phone { left: 100px; top: 327px; }
  .contact--fax { left: 100px; top: 397px; }
  .contact--web { left: 618px; top: 196px; gap: 30px; }
  .contact--email { left: 618px; top: 266px; gap: 30px; }

  .brand { position: absolute; left: 610px; top: 357px; display: flex; align-items: center; gap: 22px; }
  .brand__dot { width: 34px; height: 34px; border-radius: 50%; background: var(--mark-grey); opacity: 0.8; }
  .brand__rule { width: 2px; height: 88px; background: #a8a8a8; }
  .brand__name { font-family: "Open Sans", sans-serif; font-weight: 600; font-size: 38px; color: var(--mark-grey); letter-spacing: -1px; }

  .hours { position: absolute; left: 100px; top: 523px; font-size: 30px; line-height: 51px; }
  .hours__label { color: var(--ink); }
  .hours__day { color: var(--ink-soft); }
  .hours__time { color: var(--white); }
  .hours__gap { display: inline-block; width: 30px; }
</style>
</head>
<body>
  <div class="card">
    <div class="band band--top"></div>
    <div class="band band--middle"></div>
    <div class="band band--bottom"></div>
    <div class="stripes stripes--top"></div>
    <div class="stripes stripes--middle"></div>
    <div class="stripes stripes--bottom"></div>

    <h1 class="title">Vel's Apothecary Owner/Pharm D</h1>

    <div class="contact contact--address">
      <svg width="50" height="40" viewBox="0 0 50 40" aria-hidden="true"><path d="M25 2 L2 22 H8 V40 H20 V28 H30 V40 H42 V22 H48 Z"/><rect x="34" y="4" width="6" height="10"/></svg>
      <div>7143 North Birch Lane<br>Sioux Falls, SD 57362</div>
    </div>
    <div class="contact contact--phone">
      <svg width="46" height="38" viewBox="0 0 46 38" aria-hidden="true"><path d="M8 30 C18 38 34 26 40 12 L32 6 L28 12 C26 18 22 22 16 24 L12 20 L4 26 Z"/></svg>
      <div>605-318-6027</div>
    </div>
    <div class="contact contact--fax">
      <svg width="46" height="38" viewBox="0 0 46 38" aria-hidden="true"><rect x="2" y="4" width="10" height="32" rx="3"/><rect x="14" y="0" width="20" height="12"/><rect x="14" y="14" width="26" height="22" rx="2"/><g fill="#e6e6e6"><rect x="18" y="18" width="4" height="4"/><rect x="25" y="18" width="4" height="4"/><rect x="32" y="18" width="4" height="4"/><rect x="18" y="25" width="4" height="4"/><rect x="25" y="25" width="4" height="4"/><rect x="32" y="25" width="4" height="4"/></g></svg>
      <div>605-318-6025</div>
    </div>
    <div class="contact contact--web">
      <svg width="48" height="48" viewBox="0 0 48 48" aria-hidden="true"><circle cx="24" cy="24" r="23"/><path d="M14 10 Q22 8 24 16 Q18 20 20 26 Q12 26 10 18 Z M28 22 Q36 20 38 28 Q34 38 28 40 Q30 30 26 28 Z" fill="#e6e6e6"/></svg>
      <div>www.velsapothecary.example</div>
    </div>
    <div class="contact contact--email">
      <svg width="42" height="42" viewBox="0 0 42 42" aria-hidden="true"><rect x="0" y="0" width="42" height="42" rx="8"/><rect x="9" y="13" width="24" height="16" rx="2" fill="#e6e6e6"/><path d="M9 14 L21 23 L33 14" stroke="#333" stroke-width="2.5" fill="none"/></svg>
      <div>vel@velsapothecary.example</div>
    </div>

    <div class="brand">
      <div class="brand__dot"></div>
      <div class="brand__rule"></div>
      <div class="brand__name">Vel's Apothecary</div>
    </div>

    <div class="hours">
      <div class="hours__label">Store hours:</div>
      <div><span class="hours__day">Monday-Friday</span> <span class="hours__time">8 am - 7 pm</span><span class="hours__gap"></span><span class="hours__day">Saturday</span> <span class="hours__time">8 am - 12 pm</span></div>
      <div class="hours__time">Sunday Closed</div>
    </div>
  </div>
</body>
</html>
```